Online Charity Portal

We need a website mockup for a new project.

GiveSpark is a toolbar download that will donate a penny to your favorite charity for every search you perform. The website will be approximately 2-3 pages with the home page explaining the overall concept. One tab at the top will be FAQ's and other "Charities".

On the home page there needs to be a registration form that will collect Name, email, address, charity (from a pull down list of 20 charity names).

The site should be clean and neat with a very professional look and feel.

A site I really like and you can emulate is - https://meetpage.io/

Once completed - the code will be given to the backend developer to implement.

Industry/Entity Type

Charity

Requirements

```html
<!DOCTYPE html>
<html lang="en">
<head>
<meta charset="utf-8">
<title>GiveSpark — Donate a penny to your favorite charity</title>
<link href="https://fonts.googleapis.com/css2?family=Arimo:wght@400;700&display=swap" rel="stylesheet">
<style>
  :root {
    --black: #000000;
    --white: #ffffff;
    --orange: #ff9c00;
    --green: #84bf06;
    --ink: #111111;
    --muted: #555555;
    --field-border: #8a8a8a;
    --panel: rgba(255, 255, 255, 0.9);
  }
  * { box-sizing: border-box; margin: 0; padding: 0; }
  html, body { width: 1200px; height: 727px; overflow: hidden; }
  body {
    position: relative;
    background: var(--white);
    font-family: "Arimo", Helvetica, Arial, sans-serif;
    color: var(--ink);
  }

  /* Header */
  .site-header {
    position: absolute; left: 0; top: 0; width: 1200px; height: 34px;
    background: var(--black);
  }
  .brand {
    position: absolute; left: 122px; top: 8px;
    font-size: 17px; font-weight: 400; color: var(--white); letter-spacing: 0.2px;
  }
  .main-nav a {
    position: absolute; top: 8px; font-size: 15px; color: var(--white); text-decoration: none;
  }
  .main-nav .nav-faq { left: 920px; }
  .main-nav .nav-charities { left: 1006px; }

  /* Hero */
  .hero { position: absolute; left: 0; top: 34px; width: 1200px; height: 422px; overflow: hidden; }
  .photo-tile { position: absolute; }

  .hero-headline {
    position: absolute; left: 137px; top: 145px;
    color: var(--white); font-weight: 400; line-height: 1;
    text-transform: uppercase;
  }
  .hero-headline span {
    display: inline-block; background: var(--black); padding: 1px 3px 0;
  }
  .hero-headline .line-small { font-size: 37px; letter-spacing: -0.5px; }
  .hero-headline .line-large { font-size: 57px; letter-spacing: -1px; margin-top: 3px; }
  .hero-headline .line-last { margin-top: 3px; }

  /* Donation form */
  .donate-panel {
    position: absolute; left: 733px; top: 37px; width: 329px; height: 347px;
    background: var(--panel); border-radius: 4px;
    box-shadow: 0 0 4px rgba(0, 0, 0, 0.25);
  }
  .donate-title {
    position: absolute; left: 34px; top: 22px;
    font-size: 20px; font-weight: 400; line-height: 25px; color: #444;
  }
  .donate-title strong { font-weight: 400; color: #222; }
  .donate-title em { font-style: normal; color: var(--orange); }
  .field {
    position: absolute; left: 34px; width: 262px;
    border: 1px solid var(--field-border); background: var(--white);
    font-family: inherit; font-size: 12px; color: #333;
    padding: 7px 10px; border-radius: 1px;
  }
  .field-name { top: 81px; height: 28px; }
  .field-email { top: 118px; height: 28px; }
  .field-address { top: 156px; height: 89px; resize: none; }
  .field-select { top: 254px; height: 28px; padding: 0; }
  .field-select .select-label { position: absolute; left: 10px; top: 7px; }
  .field-select .select-arrows {
    position: absolute; right: 0; top: 0; width: 26px; height: 26px;
    border-left: 1px solid var(--field-border);
  }
  .donate-button {
    position: absolute; left: 189px; top: 292px; width: 107px; height: 27px;
    border: none; border-radius: 14px; background: var(--green);
    color: var(--white); font-family: inherit; font-size: 12px; font-weight: 700;
  }

  /* Steps */
  .steps { position: absolute; left: 0; top: 456px; width: 1200px; height: 237px; }
  .step { position: absolute; top: 37px; width: 310px; }
  .step-number {
    position: absolute; left: 0; top: 0; width: 48px; height: 48px; border-radius: 50%;
    background: var(--black); color: var(--white);
    font-size: 33px; line-height: 48px; text-align: center;
  }
  .step-title {
    position: absolute; left: 65px; top: 6px;
    font-size: 34px; font-weight: 400; color: var(--orange); line-height: 1;
  }
  .step-text {
    position: absolute; left: 67px; top: 52px; width: 240px;
    font-size: 14px; line-height: 19px; color: var(--ink);
  }

  /* Footer */
  .site-footer {
    position: absolute; left: 0; top: 693px; width: 1200px; height: 34px;
    background: var(--orange); color: var(--white); font-size: 12px;
  }
  .footer-links { position: absolute; left: 121px; top: 10px; list-style: none; display: flex; }
  .footer-links li + li::before { content: "|"; margin: 0 10px; }
  .footer-links a { color: var(--white); text-decoration: none; }
  .copyright { position: absolute; right: 120px; top: 10px; }
</style>
</head>
<body>
  <header class="site-header">
    <div class="brand">GiveSpark</div>
    <nav class="main-nav">
      <a class="nav-faq" href="#">FAQ’s</a>
      <a class="nav-charities" href="#">Charities</a>
    </nav>
  </header>

  <section class="hero">
    <div class="photo-tile" role="img" aria-label="Children holding a thank-you sign" style="left:0;top:0;width:131px;height:140px;background:linear-gradient(160deg,#c9a2a6,#8a6c70);"></div>
    <div class="photo-tile" role="img" aria-label="Child washing hands under running water" style="left:131px;top:0;width:235px;height:140px;background:linear-gradient(160deg,#b88060,#5e3a26);"></div>
    <div class="photo-tile" role="img" aria-label="Group of smiling children outdoors" style="left:366px;top:0;width:234px;height:140px;background:linear-gradient(160deg,#8f8a7c,#4f5a6a);"></div>
    <div class="photo-tile" role="img" aria-label="Children holding a thank-you sign" style="left:600px;top:0;width:234px;height:140px;background:linear-gradient(160deg,#c9a2a6,#8a6c70);"></div>
    <div class="photo-tile" role="img" aria-label="Child washing hands under running water" style="left:834px;top:0;width:235px;height:140px;background:linear-gradient(160deg,#b88060,#5e3a26);"></div>
    <div class="photo-tile" role="img" aria-label="Group of smiling children outdoors" style="left:1069px;top:0;width:131px;height:140px;background:linear-gradient(160deg,#8f8a7c,#4f5a6a);"></div>

    <div class="photo-tile" role="img" aria-label="Volunteers at a clothing drive" style="left:0;top:140px;width:131px;height:141px;background:linear-gradient(160deg,#a38a7c,#6f7a6c);"></div>
    <div class="photo-tile" role="img" aria-label="Volunteers at a clothing drive" style="left:131px;top:140px;width:235px;height:141px;background:linear-gradient(160deg,#b9a08e,#7c6f72);"></div>
    <div class="photo-tile" role="img" aria-label="Smiling children at a school" style="left:366px;top:140px;width:234px;height:141px;background:linear-gradient(160deg,#4e8a88,#6a4e3c);"></div>
    <div class="photo-tile" role="img" aria-label="Volunteers handing out clothes" style="left:600px;top:140px;width:234px;height:141px;background:linear-gradient(160deg,#6f9bb0,#8a6a50);"></div>
    <div class="photo-tile" role="img" aria-label="Smiling children at a school" style="left:834px;top:140px;width:235px;height:141px;background:linear-gradient(160deg,#4e8a88,#6a4e3c);"></div>
    <div class="photo-tile" role="img" aria-label="Smiling child" style="left:1069px;top:140px;width:131px;height:141px;background:linear-gradient(160deg,#3f8a7a,#8a5e44);"></div>

    <div class="photo-tile" role="img" aria-label="Glass jar of coins" style="left:0;top:281px;width:131px;height:141px;background:linear-gradient(160deg,#d8b9a0,#8a5e40);"></div>
    <div class="photo-tile" role="img" aria-label="Children in a classroom" style="left:131px;top:281px;width:235px;height:141px;background:linear-gradient(160deg,#8a6a55,#b6788c);"></div>
    <div class="photo-tile" role="img" aria-label="Child drinking from a red cup" style="left:366px;top:281px;width:234px;height:141px;background:linear-gradient(160deg,#b0603a,#3f5a2a);"></div>
    <div class="photo-tile" role="img" aria-label="Hand dropping a coin into a jar" style="left:600px;top:281px;width:234px;height:141px;background:linear-gradient(160deg,#d8b9a0,#8a5e40);"></div>
    <div class="photo-tile" role="img" aria-label="Children in a classroom" style="left:834px;top:281px;width:235px;height:141px;background:linear-gradient(160deg,#8a6a55,#b6788c);"></div>
    <div class="photo-tile" role="img" aria-label="Child drinking from a red cup" style="left:1069px;top:281px;width:131px;height:141px;background:linear-gradient(160deg,#b0603a,#3f5a2a);"></div>

    <h1 class="hero-headline">
      <span class="line-small">Be the source of</span><br>
      <span class="line-large">Happiness</span><br>
      <span class="line-small line-last">To others</span>
    </h1>

    <form class="donate-panel">
      <h2 class="donate-title">Donate <strong>a penny</strong> to your<br>favorite <em>charity</em></h2>
      <div class="field field-name">Name</div>
      <div class="field field-email">E-mail</div>
      <div class="field field-address">Address</div>
      <div class="field field-select">
        <span class="select-label">Charities</span>
        <svg class="select-arrows" viewBox="0 0 26 26" aria-hidden="true">
          <path d="M10 11 L13 8 L16 11 Z M10 15 L13 18 L16 15 Z" fill="#444"/>
        </svg>
      </div>
      <button class="donate-button" type="button">DONATE</button>
    </form>
  </section>

  <section class="steps">
    <div class="step" style="left:121px;">
      <div class="step-number">1</div>
      <h3 class="step-title">REGISTER</h3>
      <p class="step-text">Lorem ipsum dolor sit amet, consectetur adipisicing elit, sed do eiusmod tempor incididunt ut labore et dolore magna aliqua. Ut enim ad minim veniam, commodo consequat.</p>
    </div>
    <div class="step" style="left:449px;">
      <div class="step-number">2</div>
      <h3 class="step-title">DONATE</h3>
      <p class="step-text">Lorem ipsum dolor sit amet, consectetur adipisicing elit, sed do eiusmod tempor incididunt ut labore et dolore magna aliqua. Ut enim ad minim veniam, commodo consequat.</p>
    </div>
    <div class="step" style="left:777px;">
      <div class="step-number">3</div>
      <h3 class="step-title">CARE</h3>
      <p class="step-text">Lorem ipsum dolor sit amet, consectetur adipisicing elit, sed do eiusmod tempor incididunt ut labore et dolore magna aliqua. Ut enim ad minim veniam, commodo consequat.</p>
    </div>
  </section>

  <footer class="site-footer">
    <ul class="footer-links">
      <li><a href="#">Home</a></li>
      <li><a href="#">About Us</a></li>
      <li><a href="#">Blog</a></li>
      <li><a href="#">Terms of Use</a></li>
      <li><a href="#">Privacy Policy</a></li>
      <li><a href="#">Help</a></li>
    </ul>
    <div class="copyright">Copyright (c) GiveSpark 2013. Allrights reserved.</div>
  </footer>
</body>
</html>
```